Tallgrove Vale Management

I need a professional website. My current website is tallgrovevalemanagement.com and I hate it. It was created with some AI tool very quickly because I needed a site up and running with no advanced notice. I’m open to all designs .. I trust you, the professionals will deliver the results I’m anxiously awaiting! :)

```html
<!DOCTYPE html>
<html lang="en">
<head>
<meta charset="utf-8">
<title>Tallgrove Vale Management</title>
<link href="https://fonts.googleapis.com/css2?family=Poppins:wght@300;400;500;600;700;800&display=swap" rel="stylesheet">
<style>
:root{
  --navy:#223559;
  --navy-dark:#1b2b4a;
  --red:#c8242b;
  --red-dark:#a81c22;
  --ink:#1d1d1f;
  --text:#3b3b3f;
  --muted:#6b6b70;
  --line:#d8d8dc;
  --paper:#ffffff;
  --mist:#f1f2f4;
}
*{box-sizing:border-box;margin:0;padding:0}
html,body{width:1200px;height:4234px;overflow:hidden}
body{position:relative;background:var(--paper);font-family:"Poppins",sans-serif;color:var(--text)}
.abs{position:absolute}
a{color:inherit;text-decoration:none}
.btn{position:absolute;display:flex;align-items:center;justify-content:center;gap:8px;color:#fff;font-weight:700;font-size:16px;text-transform:uppercase;background:var(--red)}
.btn svg{width:15px;height:15px}
.btn.navy{background:var(--navy)}
.red-rule{position:absolute;height:3px;background:var(--red)}

/* top bar + header */
.topbar{left:0;top:0;width:1200px;height:44px;background:var(--navy)}
.topbar-left{left:0;top:0;width:400px;height:44px;background:#fff;clip-path:polygon(0 0,380px 0,400px 44px,0 44px)}
.topbar-slash{left:370px;top:0;width:40px;height:44px;background:var(--red);clip-path:polygon(0 0,14px 0,34px 44px,20px 44px)}
.topbar-info{top:0;height:44px;display:flex;align-items:center;gap:10px;color:#fff;font-size:17px}
.topbar-sep{left:873px;top:8px;width:1px;height:28px;background:#8793ad}
.header{left:0;top:44px;width:1200px;height:96px;background:#fff}
.brand{left:112px;top:68px;display:flex;align-items:center;gap:10px;width:220px}
.brand-mark{width:30px;height:30px;background:var(--red);flex:none}
.brand-name{font-weight:700;font-size:17px;line-height:1.15;color:var(--navy)}
.nav{left:398px;top:80px;display:flex;gap:36px;font-size:17px;font-weight:500;color:var(--ink)}
.nav .active{color:var(--red)}
.quote{left:880px;top:70px;width:209px;height:48px;font-size:16px}

/* hero */
.hero{left:0;top:140px;width:1200px;height:600px;background:linear-gradient(180deg,#1f2e52 0%,#2f4474 40%,#3b4a6e 65%,#1a2238 100%)}
.hero-title{left:112px;top:288px;color:#fff;font-size:45px;line-height:54px;text-transform:uppercase}
.hero-title b{font-weight:800}
.hero-title span{font-weight:500}
.hero-sub{left:112px;top:404px;width:580px;color:#fff;font-size:17.5px;line-height:28px}
.hero-btn{left:112px;top:477px;width:299px;height:46px}

/* why */
.why-navy{left:1047px;top:666px;width:153px;height:290px;background:var(--navy);clip-path:polygon(0 0,100% 0,100% 100%,0 195px)}
.why-red{left:0;top:690px;width:153px;height:60px;background:var(--red);clip-path:polygon(0 0,100% 40px,100% 100%)}
.why-card{left:153px;top:666px;width:894px;height:420px;background:#fff}
.h2{position:absolute;left:0;width:1200px;text-align:center;font-size:31px;color:var(--navy);text-transform:uppercase}
.h2 b{font-weight:800}
.h2 span{font-weight:400}
.why-sub{left:0;top:785px;width:1200px;text-align:center;font-size:16px;color:var(--ink)}
.feature{top:822px;width:212px;height:242px;border:2px solid #e3e3e6;border-radius:4px;background:#f7f7f8;text-align:center;padding-top:24px}
.feature svg{width:66px;height:62px}
.feature h3{margin-top:14px;font-size:18.5px;font-weight:500;line-height:23px;color:var(--navy)}
.feature p{margin-top:14px;font-size:13.5px;line-height:20px;color:var(--ink);padding:0 20px}

/* about */
.photo{position:absolute}
.about-title{left:633px;top:1218px;font-size:31px;line-height:41px;color:var(--navy);text-transform:uppercase}
.about-title b{font-weight:800}
.about-title span{font-weight:400}
.about-text{left:633px;width:470px;font-size:15.5px;line-height:26px;color:var(--ink)}

/* process */
.process{left:0;top:1825px;width:1200px;height:720px;background:var(--navy)}
.process-line{left:199px;top:2057px;width:784px;border-top:1px dashed #9aa5bd}
.step{top:2008px;width:240px;text-align:center;color:#fff}
.step-dot{margin:0 auto;width:98px;height:98px;border-radius:50%;background:var(--red);display:flex;align-items:center;justify-content:center}
.step-dot span{width:70px;height:70px;border-radius:50%;border:2px solid #fff;display:flex;align-items:center;justify-content:center}
.step h3{margin-top:20px;font-size:18.5px;font-weight:600;text-transform:uppercase}
.step p{margin:10px auto 0;width:210px;font-size:14.5px;line-height:23px}
.circle-arrow{width:30px;height:30px}

/* services */
.svc-red{left:0;top:2400px;width:110px;height:66px;background:var(--red);clip-path:polygon(0 0,100% 36px,100% 100%)}
.svc-card{left:110px;top:2343px;width:978px;height:731px;background:#fff}
.service{top:2499px;width:273px;text-align:center}
.svc-img{position:relative;width:273px;height:260px;overflow:hidden}
.svc-img .tri{position:absolute;right:0;bottom:0;width:160px;height:62px}
.service h3{margin-top:38px;font-size:19.5px;font-weight:500;color:var(--ink);text-transform:uppercase}
.service p{margin-top:10px;font-size:15px;line-height:25px;color:var(--ink);padding:0 6px}
.service .btn{position:relative;margin:24px auto 0;width:146px;height:40px;font-size:13.5px}
.chev{width:24px;height:30px}

/* form */
.proposal{left:0;top:3074px;width:1200px;height:674px;background:var(--mist)}
.field{position:absolute;background:#fff;border:1.5px solid #d8d8dc;font-size:16px;color:#555;padding:14px 15px}

/* footer */
.footer{left:0;top:3748px;width:1200px;height:486px;background:var(--navy-dark)}
.foot-brand{left:107px;top:3925px;display:flex;align-items:center;gap:14px;width:260px}
.foot-brand .brand-mark{width:40px;height:40px}
.foot-brand .brand-name{color:#fff;font-size:24px}
.foot-col{color:#fff}
.foot-col h4{font-size:21px;font-weight:500;margin-bottom:14px}
.foot-col li{list-style:none;display:flex;align-items:center;gap:12px;font-size:14.5px;height:31px}
.foot-col li svg{width:12px;height:12px}
.contact li{height:59px;gap:16px}
.pin{width:34px;height:34px;border-radius:50%;background:var(--red);display:flex;align-items:center;justify-content:center;flex:none}
.pin svg{width:16px;height:16px}
.foot-rule{left:110px;top:4162px;width:980px;height:1px;background:#3a4b6e}
.copyright{left:0;top:4193px;width:1200px;text-align:center;color:#fff;font-size:15px}
</style>
</head>
<body>

<!-- top bar -->
<div class="abs topbar"></div>
<div class="abs topbar-left"></div>
<div class="abs topbar-slash"></div>
<div class="abs topbar-info" style="left:494px">
  <svg width="18" height="14" viewBox="0 0 18 14"><rect x="0.5" y="0.5" width="17" height="13" fill="#fff"/><path d="M1 1l8 6 8-6" stroke="#223559" stroke-width="1.6" fill="none"/></svg>
  info@tallgrovevalemanagement.com
</div>
<div class="abs topbar-sep"></div>
<div class="abs topbar-info" style="left:918px">
  <svg width="16" height="16" viewBox="0 0 24 24"><path fill="#fff" d="M6.6 10.8a15.1 15.1 0 006.6 6.6l2.2-2.2a1 1 0 011-.25 11.4 11.4 0 003.6.57 1 1 0 011 1V20a1 1 0 01-1 1A17 17 0 013 4a1 1 0 011-1h3.5a1 1 0 011 1c0 1.25.2 2.45.57 3.57a1 1 0 01-.25 1z"/></svg>
  +1 555 0142 7788
</div>

<!-- header -->
<header class="abs header"></header>
<div class="abs brand"><span class="brand-mark"></span><span class="brand-name">Tallgrove Vale Management</span></div>
<nav class="abs nav">
  <a class="active" href="#">HOME</a><a href="#">SERVICES</a><a href="#">ABOUT</a><a href="#">BLOG</a><a href="#">CONTACT</a>
</nav>
<a class="btn quote" href="#">Request a Quote <svg viewBox="0 0 16 16"><circle cx="8" cy="8" r="8" fill="#fff"/><path d="M6 4.5L9.5 8 6 11.5" stroke="#c8242b" stroke-width="2" fill="none"/></svg></a>

<!-- hero -->
<div class="abs hero" role="img" aria-label="Modern hillside home at dusk with lit windows, pool and car in the driveway"></div>
<h1 class="abs hero-title"><b>Property Management</b><br><span>Built Around Performance.</span></h1>
<p class="abs hero-sub">Protecting investments, maximizing returns, and creating exceptional tenant experiences across Ohio.</p>
<a class="btn hero-btn" href="#">Schedule a Consultation <svg viewBox="0 0 16 16"><circle cx="8" cy="8" r="8" fill="#fff"/><path d="M6 4.5L9.5 8 6 11.5" stroke="#c8242b" stroke-width="2" fill="none"/></svg></a>

<!-- why -->
<div class="abs why-navy"></div>
<div class="abs why-red"></div>
<section class="abs why-card"></section>
<h2 class="h2" style="top:724px"><b>Why Property</b> <span>Owners Choose</span></h2>
<div class="red-rule" style="left:566px;top:772px;width:68px"></div>
<p class="abs why-sub">Our organization delivers comprehensive property management solutions that optimize asset</p>

<div class="abs feature" style="left:235px">
  <svg viewBox="0 0 66 62" fill="none" stroke="#223559" stroke-width="2"><path d="M14 30L33 12l19 18"/><path d="M19 26v14h28V26"/><rect x="29" y="31" width="8" height="9"/><path d="M6 46c8-4 16-4 22 0h14c3 0 3 4 0 4H30"/><path d="M6 54h30l20-10c3-2 1-6-3-4l-12 5"/></svg>
  <h3>Property<br>Management</h3>
  <p>Whether you own a single rental property or a growing portfolio</p>
</div>
<div class="abs feature" style="left:497px">
  <svg viewBox="0 0 66 62" fill="none" stroke="#223559" stroke-width="2"><path d="M10 56V26l23-14 23 14v30z"/><rect x="16" y="32" width="7" height="7"/><rect x="43" y="32" width="7" height="7"/><rect x="29" y="40" width="8" height="16"/><rect x="16" y="44" width="7" height="7"/><rect x="43" y="44" width="7" height="7"/><circle cx="46" cy="10" r="6"/></svg>
  <h3>Reliable Tenant<br>Support</h3>
  <p>Whether you own a single rental property or a growing portfolio</p>
</div>
<div class="abs feature" style="left:760px">
  <svg viewBox="0 0 66 62" fill="none" stroke="#223559" stroke-width="2"><circle cx="28" cy="16" r="7"/><circle cx="28" cy="16" r="2.5"/><circle cx="46" cy="38" r="9"/><circle cx="46" cy="38" r="3"/><path d="M6 30h22M6 38h22M6 46h28M6 54h20"/></svg>
  <h3>Fast Maintenance<br>Response</h3>
  <p>Whether you own a single rental property or a growing portfolio</p>
</div>

<!-- about -->
<div class="photo" style="left:112px;top:1224px;width:231px;height:224px;background:linear-gradient(160deg,#e9e6e1,#c9bba7 60%,#8a7864)" role="img" aria-label="Bright kitchen with white island and pendant lights"></div>
<div class="photo" style="left:356px;top:1192px;width:231px;height:256px;background:linear-gradient(170deg,#a9896a,#c8a37a 55%,#7b6a58)" role="img" aria-label="Wooden kitchen counter with white flowers and built-in oven"></div>
<div class="photo" style="left:112px;top:1462px;width:231px;height:251px;background:linear-gradient(170deg,#d8d4cf,#efedea 60%,#bdb7b0)" role="img" aria-label="Bathroom with freestanding white tub and marble wall"></div>
<div class="photo" style="left:356px;top:1462px;width:231px;height:214px;background:linear-gradient(170deg,#f0eeea,#d9d3cb 60%,#6b5442)" role="img" aria-label="Curved staircase in a bright entry hall"></div>

<h2 class="abs about-title"><b>About Our Property</b><br><span>Management Solutions</span></h2>
<div class="red-rule" style="left:633px;top:1312px;width:68px"></div>
<p class="abs about-text" style="top:1337px">Our organization delivers comprehensive property management solutions that optimize asset performance and tenant satisfaction. By integrating advanced analytics with proven operational frameworks, our specialists ensure each property achieves sustained value appreciation.</p>
<p class="abs about-text" style="top:1491px">Drawing on decades of collective expertise, the team facilitates regulatory compliance, cost efficiency, and proactive maintenance.</p>
<a class="btn" href="#" style="left:633px;top:1590px;width:169px;height:46px">Learn More <svg viewBox="0 0 16 16"><circle cx="8" cy="8" r="8" fill="#fff"/><path d="M6 4.5L9.5 8 6 11.5" stroke="#c8242b" stroke-width="2" fill="none"/></svg></a>

<!-- process -->
<section class="abs process"></section>
<h2 class="h2" style="top:1915px;color:#fff"><span>Our</span> <b>Process</b></h2>
<div class="red-rule" style="left:566px;top:1958px;width:68px"></div>
<div class="abs process-line"></div>
<svg class="abs circle-arrow" style="left:43px;top:2114px" viewBox="0 0 30 30" fill="none" stroke="#fff" stroke-width="1.6"><circle cx="15" cy="15" r="13"/><path d="M17 9l-6 6 6 6"/></svg>
<svg class="abs circle-arrow" style="left:1126px;top:2114px" viewBox="0 0 30 30" fill="none" stroke="#fff" stroke-width="1.6"><circle cx="15" cy="15" r="13"/><path d="M13 9l6 6-6 6"/></svg>

<div class="abs step" style="left:79px">
  <div class="step-dot"><span><svg width="32" height="32" viewBox="0 0 32 32" fill="#fff"><circle cx="11" cy="12" r="4"/><path d="M4 26c0-5 3-8 7-8s7 3 7 8z"/><circle cx="22" cy="14" r="3.5"/><path d="M16 26c0-4 3-7 6-7s6 3 6 7z"/><rect x="18" y="3" width="10" height="6" rx="1"/></svg></span></div>
  <h3>Consultation</h3>
  <p>We learn about your property, your goals, and your expectations.</p>
</div>
<div class="abs step" style="left:337px">
  <div class="step-dot"><span><svg width="32" height="32" viewBox="0 0 32 32" fill="none" stroke="#fff" stroke-width="2"><path d="M4 15L16 5l12 10"/><path d="M8 13v13h16V13"/><rect x="13" y="18" width="6" height="8" fill="#fff"/></svg></span></div>
  <h3>Property Assessment</h3>
  <p>Our team evaluates your property and develops a customized</p>
</div>
<div class="abs step" style="left:597px">
  <div class="step-dot"><span><svg width="32" height="32" viewBox="0 0 32 32" fill="none" stroke="#fff" stroke-width="2"><circle cx="16" cy="16" r="11"/><circle cx="16" cy="16" r="4"/><path d="M16 3v5M16 24v5M3 16h5M24 16h5"/></svg></span></div>
  <h3>Management Setup</h3>
  <p>We coordinate the transition, organize documentation, and prepare your property</p>
</div>
<div class="abs step" style="left:863px">
  <div class="step-dot"><span><svg width="32" height="32" viewBox="0 0 32 32" fill="#fff"><rect x="6" y="16" width="5" height="11"/><rect x="14" y="10" width="5" height="17"/><rect x="22" y="13" width="5" height="14"/><path d="M16 2l5 6h-10z"/></svg></span></div>
  <h3>Ongoing Management</h3>
  <p>We manage daily operations, communicate with tenants</p>
</div>

<!-- services -->
<div class="abs svc-red"></div>
<section class="abs svc-card"></section>
<div class="abs" style="left:1088px;top:2343px;width:112px;height:240px;background:var(--navy);clip-path:polygon(0 0,100% 0,100% 100%,0 190px)"></div>
<h2 class="h2" style="top:2410px"><span>Our</span> <b>Services</b></h2>
<div class="red-rule" style="left:566px;top:2454px;width:68px"></div>
<svg class="abs chev" style="left:65px;top:2711px" viewBox="0 0 24 30" fill="none" stroke="#1d1d1f" stroke-width="2"><path d="M16 4L6 15l10 11"/></svg>
<svg class="abs chev" style="left:1111px;top:2711px" viewBox="0 0 24 30" fill="none" stroke="#1d1d1f" stroke-width="2"><path d="M8 4l10 11-10 11"/></svg>

<div class="abs service" style="left:150px">
  <div class="svc-img" role="img" aria-label="Hands arranging material samples on a wooden table" style="background:linear-gradient(160deg,#b59473,#d9c1a3 50%,#8c6c52)">
    <svg class="tri" viewBox="0 0 160 62" preserveAspectRatio="none"><path d="M160 0V62H0z" fill="#223559"/></svg>
  </div>
  <h3>Basic Service</h3>
  <p>Describe important details like price, value, length of service, and why it’s unique.</p>
  <a class="btn navy" href="#">Learn More <svg viewBox="0 0 16 16"><circle cx="8" cy="8" r="8" fill="#fff"/><path d="M6 4.5L9.5 8 6 11.5" stroke="#223559" stroke-width="2" fill="none"/></svg></a>
</div>
<div class="abs service" style="left:464px">
  <div class="svc-img" role="img" aria-label="Round table lamp on a desk beside a notebook" style="background:linear-gradient(160deg,#c7b7a4,#e6dccd 55%,#2b2a2a)">
    <svg class="tri" viewBox="0 0 160 62" preserveAspectRatio="none"><path d="M160 0V62H0z" fill="#c8242b"/></svg>
  </div>
  <h3>Intermediate Service</h3>
  <p>Describe important details like price, value, length of service, and why it’s unique.</p>
  <a class="btn" href="#">Learn More <svg viewBox="0 0 16 16"><circle cx="8" cy="8" r="8" fill="#fff"/><path d="M6 4.5L9.5 8 6 11.5" stroke="#c8242b" stroke-width="2" fill="none"/></svg></a>
</div>
<div class="abs service" style="left:778px">
  <div class="svc-img" role="img" aria-label="Desk with white lilies in a vase and a small lamp" style="background:linear-gradient(160deg,#8d7b69,#d7cbbd 55%,#b9ab9b)">
    <svg class="tri" viewBox="0 0 160 62" preserveAspectRatio="none"><path d="M160 0V62H0z" fill="#223559"/></svg>
  </div>
  <h3>Advanced Service</h3>
  <p>Describe important details like price, value, length of service, and why it’s unique.</p>
  <a class="btn navy" href="#">Learn More <svg viewBox="0 0 16 16"><circle cx="8" cy="8" r="8" fill="#fff"/><path d="M6 4.5L9.5 8 6 11.5" stroke="#223559" stroke-width="2" fill="none"/></svg></a>
</div>

<!-- proposal form -->
<section class="abs proposal"></section>
<h2 class="h2" style="top:3160px"><span>Request a</span> <b>Tailored Proposal</b></h2>
<p class="abs" style="left:0;top:3238px;width:1200px;text-align:center;font-size:16px;color:var(--ink)">Submit the form to initiate a consultative assessment and explore solutions aligned with your objectives.</p>
<div class="field" style="left:127px;top:3293px;width:463px;height:53px">First Name</div>
<div class="field" style="left:610px;top:3293px;width:464px;height:53px">Last Name</div>
<div class="field" style="left:127px;top:3369px;width:463px;height:52px">Email</div>
<div class="field" style="left:610px;top:3369px;width:464px;height:52px">Address</div>
<div class="field" style="left:127px;top:3444px;width:945px;height:123px">Message</div>
<a class="btn" href="#" style="left:449px;top:3589px;width:301px;height:46px">Schedule a Consultation <svg viewBox="0 0 16 16"><circle cx="8" cy="8" r="8" fill="#fff"/><path d="M6 4.5L9.5 8 6 11.5" stroke="#c8242b" stroke-width="2" fill="none"/></svg></a>

<!-- footer -->
<footer class="abs footer"></footer>
<div class="abs foot-brand"><span class="brand-mark"></span><span class="brand-name">Tallgrove Vale Management</span></div>

<div class="abs foot-col" style="left:422px;top:3858px">
  <h4>Quick Links</h4>
  <ul>
    <li><svg viewBox="0 0 12 12"><path d="M0 5h7V2l5 4-5 4V7H0z" fill="#fff"/></svg>Home</li>
    <li><svg viewBox="0 0 12 12"><path d="M0 5h7V2l5 4-5 4V7H0z" fill="#fff"/></svg>About Us</li>
    <li><svg viewBox="0 0 12 12"><path d="M0 5h7V2l5 4-5 4V7H0z" fill="#fff"/></svg>Services</li>
    <li><svg viewBox="0 0 12 12"><path d="M0 5h7V2l5 4-5 4V7H0z" fill="#fff"/></svg>Blog</li>
    <li><svg viewBox="0 0 12 12"><path d="M0 5h7V2l5 4-5 4V7H0z" fill="#fff"/></svg>Contact Us</li>
  </ul>
</div>
<div class="abs foot-col" style="left:621px;top:3858px">
  <h4>Other Links</h4>
  <ul>
    <li><svg viewBox="0 0 12 12"><path d="M0 5h7V2l5 4-5 4V7H0z" fill="#fff"/></svg>FAQ</li>
    <li><svg viewBox="0 0 12 12"><path d="M0 5h7V2l5 4-5 4V7H0z" fill="#fff"/></svg>Terms of Use</li>
    <li><svg viewBox="0 0 12 12"><path d="M0 5h7V2l5 4-5 4V7H0z" fill="#fff"/></svg>Privacy Policy</li>
    <li><svg viewBox="0 0 12 12"><path d="M0 5h7V2l5 4-5 4V7H0z" fill="#fff"/></svg>Support Links</li>
    <li><svg viewBox="0 0 12 12"><path d="M0 5h7V2l5 4-5 4V7H0z" fill="#fff"/></svg>Conditions</li>
  </ul>
</div>
<div class="abs foot-col contact" style="left:832px;top:3858px">
  <h4>Contact Us</h4>
  <ul>
    <li><span class="pin"><svg viewBox="0 0 16 16"><path d="M8 1a5 5 0 015 5c0 4-5 9-5 9S3 10 3 6a5 5 0 015-5z" fill="#fff"/><circle cx="8" cy="6" r="1.8" fill="#c8242b"/></svg></span>Company Name, United State.</li>
    <li><span class="pin"><svg viewBox="0 0 16 16"><rect x="1" y="3" width="14" height="10" fill="#fff"/><path d="M1.5 3.5L8 9l6.5-5.5" stroke="#c8242b" stroke-width="1.4" fill="none"/></svg></span>hello@tallgrovevale.example</li>
    <li><span class="pin"><svg viewBox="0 0 24 24"><path fill="#fff" d="M6.6 10.8a15.1 15.1 0 006.6 6.6l2.2-2.2a1 1 0 011-.25 11.4 11.4 0 003.6.57 1 1 0 011 1V20a1 1 0 01-1 1A17 17 0 013 4a1 1 0 011-1h3.5a1 1 0 011 1c0 1.25.2 2.45.57 3.57a1 1 0 01-.25 1z"/></svg></span>+1 555 0142 7788</li>
  </ul>
</div>
<div class="abs foot-rule"></div>
<p class="abs copyright">Copyrights@2026.Company Name.All Rights Reserved</p>

</body>
</html>
```